LOGO DESIGN: Construction Related Service Business

We require a logo for our business Tovar Services. We are a construction related business offering a range of services including machine services for groundworks (digging trenches, soak wells, preparing land for construction etc), demolition and truck haulage from demolition sites.
We would like our logo to be predominately text, but may include abstract graphics. The colour scheme should be mainly a mid bright blue and overall be quite 'clean'.

Industry/Entity Type

Construction

Contact Information for Business Card

Dale Morrow
Ph:041 592 3068
tovarservices@quillnet.com.au

Colors
0456a3

```html
<!DOCTYPE html>
<html lang="en">
<head>
<meta charset="utf-8">
<title>Tovar Services – Business Card</title>
<link rel="stylesheet" href="https://fonts.googleapis.com/css2?family=Questrial&display=swap">
<style>
  :root {
    --brand-blue: #2f5fb8;
    --brand-blue-bright: #4a78d0;
    --ink: #1d1d1f;
    --band-navy: #0c1220;
    --band-black: #05070c;
    --card-white: #ffffff;
    --card-shade: #eceef1;
    --page-bg: #e4e5e8;
    --machine-grey: #d9dadc;
  }
  * { margin: 0; padding: 0; box-sizing: border-box; }
  html, body {
    width: 1200px;
    height: 800px;
    overflow: hidden;
    background: var(--page-bg);
    font-family: "Questrial", "Century Gothic", sans-serif;
  }
  .card {
    position: absolute;
    left: 180px;
    top: 160px;
    width: 840px;
    height: 480px;
    background: linear-gradient(180deg, var(--card-white) 0%, var(--card-white) 25%, var(--card-shade) 45%, var(--card-white) 70%);
    box-shadow: 0 10px 30px rgba(0,0,0,0.18);
    overflow: hidden;
  }
  .brand-name {
    position: absolute;
    left: 70px;
    top: 92px;
    font-size: 58px;
    color: var(--brand-blue);
    letter-spacing: 0.01em;
  }
  .machine-art {
    position: absolute;
    right: 40px;
    top: 20px;
    width: 200px;
    height: 300px;
    background: radial-gradient(ellipse at 50% 55%, var(--machine-grey) 0%, rgba(217,218,220,0.5) 55%, rgba(217,218,220,0) 80%);
  }
  .contact-name {
    position: absolute;
    left: 70px;
    top: 262px;
    font-size: 32px;
    color: var(--brand-blue);
  }
  .contact-list {
    position: absolute;
    left: 70px;
    top: 318px;
    list-style: none;
  }
  .contact-item {
    display: flex;
    align-items: center;
    gap: 12px;
    font-size: 27px;
    color: var(--ink);
    line-height: 38px;
  }
  .contact-icon { width: 24px; height: 24px; flex: none; }
  .tagline-band {
    position: absolute;
    left: 0;
    bottom: 0;
    width: 100%;
    height: 78px;
    background: linear-gradient(180deg, var(--band-navy), var(--band-black));
    border-top: 5px solid var(--brand-blue-bright);
    display: flex;
    align-items: center;
    padding-left: 40px;
  }
  .tagline {
    font-size: 21px;
    letter-spacing: 0.42em;
    color: var(--brand-blue-bright);
    white-space: nowrap;
  }
</style>
</head>
<body>
  <main class="card">
    <div class="brand-name">Tovar Services</div>
    <div class="machine-art" role="img" aria-label="Faint grey silhouette of an excavator arm and bucket"></div>

    <div class="contact-name">Dale Morrow</div>
    <ul class="contact-list">
      <li class="contact-item">
        <svg class="contact-icon" viewBox="0 0 24 24" aria-hidden="true">
          <path fill="#2f5fb8" d="M6.6 10.8c1.4 2.8 3.8 5.1 6.6 6.6l2.2-2.2c.3-.3.7-.4 1-.2 1.1.4 2.3.6 3.6.6.6 0 1 .4 1 1V20c0 .6-.4 1-1 1C10.6 21 3 13.4 3 4c0-.6.4-1 1-1h3.5c.6 0 1 .4 1 1 0 1.3.2 2.5.6 3.6.1.3 0 .7-.2 1z"/>
        </svg>
        <span>041 592 3068</span>
      </li>
      <li class="contact-item">
        <svg class="contact-icon" viewBox="0 0 24 24" aria-hidden="true">
          <rect x="2" y="5" width="20" height="14" rx="2" fill="#2f5fb8"/>
          <path d="M3 7l9 6 9-6" fill="none" stroke="#ffffff" stroke-width="1.8"/>
        </svg>
        <span>tovarservices@quillnet.com.au</span>
      </li>
    </ul>

    <div class="tagline-band">
      <p class="tagline">WHATEVER THE SITE...WE GET IT MOVING</p>
    </div>
  </main>
</body>
</html>
```